Two Rollup Banners Promoting Trade Association

UPDATE: Please do not recycle the prior designs we've had. I am looking for creativity and a new look. Otherwise, I would use the prior designers to just update their work.
I need two 48"x79" Pull Up Retractable Banners Designed.
One promotes the benefits of membership in the Residential Capital Partners Forum. The second promotes RCPF's role in the affordable housing ecosystem.
The content for each is attached. I'm also providing examples of two banners we recently created for our 30th Anniversary as well as some photos of our members if you choose to use them (although it's not necessary - just providing them as an option).
The banners don't have to mimic the ones we did for our 30th Anniversary. I'm simply providing them as examples of designs that meet the look and feel of our brand.
I've also provided our brand guidelines and the specs for the banner.
Updates
All,
We are looking for clean, modern, streamlined designs. No clip art. No waves. Don’t bury the message in the graphics.
Please keep that in mind as you submit designs.
Look and feel
Each slider illustrates characteristics of the customer's brand and the style your logo design should communicate.

```html
<!DOCTYPE html>
<html lang="en">
<head>
<meta charset="utf-8">
<title>RCPF Rollup Banners</title>
<link href="https://fonts.googleapis.com/css2?family=Fira+Sans+Condensed:wght@600&family=Rubik:wght@300;400;500&family=Oswald:wght@500&display=swap" rel="stylesheet">
<style>
:root{
  --orange:#e4722f;
  --orange-band:#e57534;
  --grey:#5f666b;
  --text:#4a4f54;
  --rule:#b8bcbf;
  --paper:#ffffff;
}
*{margin:0;padding:0;box-sizing:border-box}
html,body{width:1200px;height:972px;overflow:hidden;background:var(--paper)}
body{position:relative;font-family:"Rubik",sans-serif;color:var(--text)}
.banner{position:absolute;top:0;width:578px;height:972px;background:var(--paper);border-left:1px solid var(--rule);border-right:1px solid var(--rule);overflow:hidden}
.banner--membership{left:0}
.banner--ecosystem{left:622px}
.band{position:absolute;left:0;top:0;width:100%;height:37px;background:var(--orange-band)}
.brand{position:absolute;left:54px;top:84px;display:flex;align-items:center;gap:14px}
.brand__square{width:78px;height:78px;background:var(--orange-band)}
.brand__name{font-family:"Oswald",sans-serif;font-weight:500;font-size:96px;line-height:96px;color:var(--grey);letter-spacing:-1px}
.brand__rule{width:1px;height:96px;background:var(--rule);margin-left:6px}
.brand__full{font-family:"Oswald",sans-serif;font-weight:500;font-size:17px;line-height:19px;color:var(--grey);text-transform:uppercase;letter-spacing:1px;width:170px}
.heading{position:absolute;font-family:"Fira Sans Condensed",sans-serif;font-weight:600;color:var(--orange);text-transform:uppercase;line-height:1.08}
.heading--main{font-size:30px}
.heading--section{font-size:31px;letter-spacing:.5px}
.copy{position:absolute;font-size:17px;line-height:24px;font-weight:300;color:var(--text)}
.copy b{font-weight:500}
.bullets{list-style:none}
.bullets li{line-height:30px;font-size:17px}
.bullets li::before{content:"•";margin-right:8px}
.stats p{margin-bottom:6px}
.cta{position:absolute;font-weight:500;font-size:17px;line-height:20px;color:var(--orange);text-transform:uppercase}
.photo{position:absolute;left:0;top:661px;width:100%;height:311px}
.photo--handover{background:linear-gradient(160deg,#3a3b3e 0%,#23252a 45%,#d9d9d9 80%,#efefef 100%)}
.photo--city{background:radial-gradient(circle at 55% 30%,#6fa8d8 0%,#8fc25a 30%,#f6d84e 60%,#f0c63a 100%)}
</style>
</head>
<body>

<section class="banner banner--membership">
  <div class="band"></div>
  <div class="brand">
    <div class="brand__square"></div>
    <div class="brand__name">RCPF</div>
    <div class="brand__rule"></div>
    <div class="brand__full">Residential Capital Partners Forum</div>
  </div>
  <h1 class="heading heading--main" style="left:45px;top:213px">LIHTC Investor-Only Community</h1>
  <h2 class="heading heading--section" style="left:147px;top:261px">Where Investors</h2>
  <div class="copy" style="left:147px;top:298px">
    <p><b>Network:</b> Peer Groups &amp; Forums</p>
    <p><b>Learn:</b> Conferences &amp; Webinars</p>
    <p><b>Share:</b> Candid Investor-Only Exchange</p>
    <p><b>Shape:</b> Industry Standards &amp; Best Practices</p>
    <p><b>Grow:</b> Professional Development &amp;<br>Emerging Leaders Program</p>
  </div>
  <h2 class="heading heading--section" style="left:147px;top:457px">Our Community</h2>
  <div class="copy" style="left:147px;top:493px;width:400px">
    <p><b>60+</b> Investor Firms &nbsp;&nbsp; <b>1,000+</b> Industry Professionals</p>
    <p><b>Banks</b> (Large &amp; Small), <b>Insurance</b> Companies, <b>Economic</b> Investors</p>
  </div>
  <div class="cta" style="left:147px;top:606px">Join Us Today<br>www.rcpf.org</div>
  <div class="photo photo--handover" role="img" aria-label="Photo of two people handing over a small paper model house above mortgage paperwork"></div>
</section>

<section class="banner banner--ecosystem">
  <div class="band"></div>
  <div class="brand">
    <div class="brand__square"></div>
    <div class="brand__name">RCPF</div>
    <div class="brand__rule"></div>
    <div class="brand__full">Residential Capital Partners Forum</div>
  </div>
  <h1 class="heading heading--main" style="left:128px;top:210px;font-size:31px">Where LIHTC Investing<br>Excellence Begins</h1>
  <ul class="copy bullets" style="left:128px;top:280px">
    <li>Setting Industry Standards &amp; Best Practices</li>
    <li>Building Community Through Candid Exchange</li>
    <li>Promoting the Investor Perspective</li>
    <li>Fostering Collaboration Across the Ecosystem</li>
  </ul>
  <h2 class="heading heading--section" style="left:128px;top:418px">30 Years of Impact</h2>
  <div class="copy stats" style="left:128px;top:454px;width:410px">
    <p><b>Industry-Adopted Standards</b> in Underwriting, Asset Management, Risk Rating &amp; More</p>
    <p><b>4 Million</b> Rental Homes Created</p>
    <p><b>9.28 Million</b> Low-Income Households Served</p>
  </div>
  <div class="cta" style="left:128px;top:606px">Join Us Today<br>www.rcpf.org</div>
  <div class="photo photo--city" role="img" aria-label="Photo of miniature paper apartment towers, small trees and two tiny figures in front of a clay globe on a yellow background"></div>
</section>

</body>
</html>
```